Design an Elegant MAISONLEAF Brand website

I need a webiste design are looking for ideas for a new theme, color scheme, etc. You come up with the general look and feel of the home page and our team will take it from there.
We're only looking for a one (1) page layout which should be fashionable and graphic intensive, but also include the standard homepage links (about us, see our collections, etc)

Target Market(s)

Our customers are fashionable women looking for an animal friendly and environmentally friendly handbag.

Industry/Entity Type

Business

Number of Pages Required

1 page

Font styles to use
Serif
Sans Serif

Requirements
Must have
• Feel free to modify it with different colors or tweaks as you see fit. We are open to all suggestions.
Nice to have

```html
<!DOCTYPE html>
<html lang="en">
<head>
<meta charset="utf-8">
<title>Maisonleaf — Handbags</title>
<link href="https://fonts.googleapis.com/css2?family=Michroma&family=Arimo:ital,wght@0,400;0,700;1,400&display=swap" rel="stylesheet">
<style>
:root{
  --green:#0e5a47;
  --green-dark:#0a4737;
  --ink:#1d1d1d;
  --grey:#8a8a8a;
  --line:#e3e3e3;
  --band:#f2f2f2;
  --footer:#1e1e1e;
  --white:#ffffff;
  --star:#f2c21b;
}
*{box-sizing:border-box;margin:0;padding:0}
html,body{width:1200px;height:4354px;overflow:hidden;background:var(--white)}
body{position:relative;font-family:Arimo,Arial,sans-serif;color:var(--ink)}
.abs{position:absolute}
.display{font-family:Michroma,Arial,sans-serif;letter-spacing:5px;text-transform:uppercase}
.btn{display:inline-flex;align-items:center;justify-content:center;background:var(--green);color:var(--white);font-size:12px;text-transform:uppercase;letter-spacing:.3px;border:1px solid var(--green)}
.btn.outline{background:var(--white);color:var(--green)}

/* header */
.site-header{top:0;left:0;width:1200px;height:72px}
.brand{left:40px;top:14px;display:flex;align-items:center;gap:10px}
.brand-mark{width:30px;height:30px;border:2px solid var(--green);border-radius:50%}
.brand-name{font-family:Michroma,Arial,sans-serif;font-size:18px;color:var(--green);letter-spacing:2px;line-height:1}
.brand-slogan{font-size:10px;letter-spacing:4px;color:var(--green);margin-top:4px}
.main-nav{left:388px;top:33px;display:flex;gap:38px;font-size:12px;letter-spacing:.6px}
.main-nav a{color:#444;text-decoration:none;position:relative}
.main-nav a.active::after{content:"";position:absolute;left:-3px;right:-3px;top:34px;height:3px;background:var(--green)}
.header-tools{left:986px;top:30px;display:flex;gap:30px}

/* hero */
.hero{left:35px;top:73px;width:1126px;height:608px;background:linear-gradient(100deg,#6e6c77 0%,#4d5d86 35%,#8aa0cc 55%,#e8b9bf 72%,#d9a5ad 85%,#7c6a66 100%)}
.hero-title{left:80px;top:232px;font-size:46px;color:var(--white);letter-spacing:6px}
.hero-slogan{left:82px;top:288px;font-size:19px;color:var(--white);letter-spacing:8px}
.hero .btn{position:absolute;left:80px;top:334px;width:151px;height:38px}
.slider-arrow{width:36px;height:72px}
.dots{display:flex;gap:6px}
.dots span{width:9px;height:9px;border-radius:50%;background:var(--white)}
.dots span.on{background:var(--green);border:1px solid var(--white)}

/* features */
.features{top:717px;left:120px;width:960px;display:flex;justify-content:space-between}
.feature{display:flex;gap:14px;width:300px}
.feature h3{font-family:Michroma,Arial,sans-serif;font-size:13px;letter-spacing:2px;margin-bottom:6px}
.feature p{font-size:11px;color:var(--grey);line-height:14px}

/* section titles */
.section-title{left:0;width:1200px;text-align:center}
.section-title h2{font-size:25px;font-weight:400}
.section-title p{font-size:11.5px;color:var(--grey);margin-top:8px;letter-spacing:.5px}

/* products */
.product-grid{left:37px;width:1126px;display:flex;justify-content:space-between}
.product{width:263px}
.product-photo{position:relative;height:339px;border:1px solid var(--line);display:flex;align-items:center;justify-content:center}
.product-photo .shot{width:170px;height:130px;border-radius:14px}
.product-photo .fav{position:absolute;right:12px;top:18px}
.product h4{font-size:12px;font-weight:400;margin:26px 0 12px 4px;text-transform:uppercase}
.product p{font-size:11px;color:var(--grey);line-height:14px;margin-left:4px}
.product .price{font-size:17px;color:var(--ink);margin:15px 0 12px 4px}
.product .btn{width:120px;height:35px;margin-left:4px}

/* about */
.about-band{left:35px;top:1592px;width:1126px;height:370px;background:var(--band)}
.about-photo{left:84px;top:1561px;width:512px;height:343px;border:5px solid var(--white);box-shadow:0 2px 10px rgba(0,0,0,.2);background:linear-gradient(120deg,#d8a98e 0%,#c98d72 50%,#f0a89a 100%)}
.about-copy{left:663px;top:1650px;width:440px}
.about-copy h2{font-size:25px;font-weight:400}
.about-copy .sub{font-size:11px;color:var(--grey);margin-top:10px}
.about-copy .body{font-size:11.5px;color:#444;line-height:18px;margin-top:40px}
.about-copy .btn{width:120px;height:35px;margin-top:26px}

/* reviews */
.reviews{left:37px;top:2682px;width:1124px;height:370px;background:linear-gradient(90deg,#5a2b22 0%,#6b3a2e 30%,#3e4552 60%,#2e3440 100%);color:var(--white);text-align:center}
.reviews-inner{position:absolute;left:0;top:0;width:100%;height:100%;background:rgba(0,0,0,.35)}
.reviews h2{font-size:24px;font-weight:400;margin-top:62px}
.reviews .sub{font-size:11.5px;letter-spacing:2px;margin-top:8px}
.reviews .quote{width:840px;margin:22px auto 0;font-size:12px;line-height:18px}
.reviews .author{font-size:12px;letter-spacing:2px;margin-top:20px}
.reviews .stars{color:var(--star);font-size:14px;letter-spacing:2px;margin-top:2px}
.reviews .dots{position:absolute;left:537px;top:313px}

/* blogs */
.blog-grid{left:35px;top:3190px;width:1126px;display:flex;justify-content:space-between}
.post{width:358px}
.post-photo{height:270px}
.post .date{font-size:11px;color:var(--grey);margin:31px 0 0 5px}
.post h3{font-family:Michroma,Arial,sans-serif;font-size:15px;font-weight:400;letter-spacing:2px;margin:12px 0 0 5px}
.post p{font-size:11.5px;color:#444;line-height:22px;margin:18px 0 0 5px;width:340px}
.post .more{font-size:11.5px;color:var(--green);margin:20px 0 0 5px;text-transform:uppercase}
.browse{left:533px;top:3724px;width:129px;height:37px}

/* newsletter */
.newsletter-form{left:373px;top:3930px;display:flex;gap:5px}
.newsletter-form .field{width:317px;height:36px;border:1px solid #9a9a9a;font-size:11.5px;font-style:italic;color:#aaa;padding:11px 16px}
.newsletter-form .btn{width:128px;height:36px}

/* footer */
.site-footer{left:35px;top:4046px;width:1128px;height:268px;background:var(--footer);color:var(--white)}
.footer-brand{left:453px;top:48px;display:flex;align-items:center;gap:10px}
.footer-brand .brand-mark{border-color:var(--white)}
.footer-brand .brand-name{color:var(--white)}
.footer-brand .brand-slogan{color:var(--white)}
.footer-nav{left:42px;top:112px;display:flex;gap:28px;font-size:11.5px}
.socials{left:915px;top:110px;display:flex;gap:10px}
.socials span{width:18px;height:18px;background:#3b6fb6;border-radius:2px}
.footer-rule{left:42px;top:137px;width:1044px;height:1px;background:#555}
.payments{left:455px;top:163px;display:flex;gap:6px}
.payments span{width:30px;height:18px;background:#e6e6e6;border-radius:2px}
.legal{left:0;top:198px;width:1128px;text-align:center;font-size:11.5px}
</style>
</head>
<body>

<header class="site-header abs">
  <div class="brand abs">
    <span class="brand-mark"></span>
    <div>
      <div class="brand-name">MAISONLEAF</div>
      <div class="brand-slogan">Your Slogan here</div>
    </div>
  </div>
  <nav class="main-nav abs">
    <a class="active">HOME</a><a>HANDBAGS</a><a>BLOG</a><a>ABOUT</a><a>CONTACT</a>
  </nav>
  <div class="header-tools abs">
    <svg width="18" height="18" viewBox="0 0 18 18" fill="none" stroke="#333" stroke-width="1.6"><circle cx="7.5" cy="7.5" r="5.5"/><path d="M12 12l5 5"/></svg>
    <svg width="20" height="18" viewBox="0 0 20 18" fill="none" stroke="#333" stroke-width="1.6"><path d="M10 16S2 11 2 6a4 4 0 0 1 8-1 4 4 0 0 1 8 1c0 5-8 10-8 10z"/></svg>
    <svg width="18" height="18" viewBox="0 0 18 18" fill="none" stroke="#333" stroke-width="1.6"><circle cx="9" cy="5.5" r="4"/><path d="M2 17c0-4 3-6 7-6s7 2 7 6z"/></svg>
    <svg width="26" height="20" viewBox="0 0 26 20" fill="none" stroke="#333" stroke-width="1.6"><path d="M2 7h14l-1.5 11h-11z"/><path d="M6 7a3 4 0 0 1 6 0"/><text x="19" y="19" font-size="9" fill="#333" stroke="none" font-family="Arimo,Arial,sans-serif">0</text></svg>
  </div>
</header>

<section class="hero abs" role="img" aria-label="Woman in a blue dress holding a pink structured handbag">
  <h1 class="hero-title abs display">Handbags</h1>
  <p class="hero-slogan abs">That suits you everytime</p>
  <span class="btn">View Collection</span>
  <svg class="slider-arrow abs" style="left:0;top:232px" viewBox="0 0 36 72"><path d="M0 0L36 36L0 72z" fill="#fff"/><path d="M10 31l-5 5 5 5" stroke="#999" stroke-width="1.5" fill="none"/></svg>
  <svg class="slider-arrow abs" style="right:0;top:232px" viewBox="0 0 36 72"><path d="M36 0L0 36L36 72z" fill="#fff"/><path d="M26 31l5 5-5 5" stroke="#0e5a47" stroke-width="2" fill="none"/></svg>
  <div class="dots abs" style="left:538px;top:575px"><span class="on"></span><span></span><span></span><span></span></div>
</section>

<section class="features abs">
  <div class="feature">
    <svg width="56" height="34" viewBox="0 0 56 34" fill="none" stroke="#333" stroke-width="1.4"><path d="M14 8h24v18H14zM38 14h9l6 7v5h-15"/><circle cx="20" cy="28" r="3"/><circle cx="45" cy="28" r="3"/><path d="M2 14h9M5 19h7"/></svg>
    <div><h3>Free Delivery</h3><p>Lorem Ipsum is simply dummy text of the printing and typesetting industry.</p></div>
  </div>
  <div class="feature">
    <svg width="44" height="40" viewBox="0 0 44 40" fill="none" stroke="#333" stroke-width="1.6"><path d="M6 22a16 16 0 0 1 32 0"/><rect x="3" y="20" width="6" height="10" rx="2"/><rect x="35" y="20" width="6" height="10" rx="2"/><path d="M38 30c0 5-8 7-14 7"/></svg>
    <div><h3>Support 24/7 Hours</h3><p>Lorem Ipsum is simply dummy text of the printing and typesetting industry.</p></div>
  </div>
  <div class="feature">
    <svg width="36" height="40" viewBox="0 0 36 40" fill="none" stroke="#333" stroke-width="1.5"><path d="M4 12l14-8 14 8v16l-14 8-14-8z"/><path d="M4 12l14 8 14-8M18 20v16"/><path d="M9 8l14 8"/></svg>
    <div><h3>Return Policy</h3><p>Lorem Ipsum is simply dummy text of the printing and typesetting industry.</p></div>
  </div>
</section>

<div class="section-title abs" style="top:862px"><h2 class="display">Latest Products</h2><p>EXPLORE THE BEST COLLECTION HERE</p></div>

<section class="product-grid abs" style="top:945px">
  <article class="product"><div class="product-photo"><div class="shot" role="img" aria-label="Burgundy leather top-handle handbag" style="background:linear-gradient(#a2232a,#6e1216)"></div></div><h4>Products Name</h4><p>Lorem Ipsum is simply dummy text of the printing and typesetting industry.</p><div class="price">$149.99</div><span class="btn">Add to Cart</span></article>
  <article class="product"><div class="product-photo"><svg class="fav" width="18" height="16" viewBox="0 0 20 18" fill="none" stroke="#333" stroke-width="1.6"><path d="M10 16S2 11 2 6a4 4 0 0 1 8-1 4 4 0 0 1 8 1c0 5-8 10-8 10z"/></svg><div class="shot" role="img" aria-label="Taupe textured envelope clutch" style="height:95px;background:linear-gradient(#c79d87,#9e7462)"></div></div><h4>Products Name</h4><p>Lorem Ipsum is simply dummy text of the printing and typesetting industry.</p><div class="price">$149.99</div><span class="btn outline">Add to Cart</span></article>
  <article class="product"><div class="product-photo"><div class="shot" role="img" aria-label="Yellow and navy crossbody satchel" style="background:linear-gradient(#f0c43a,#d9a51c)"></div></div><h4>Products Name</h4><p>Lorem Ipsum is simply dummy text of the printing and typesetting industry.</p><div class="price">$149.99</div><span class="btn">Add to Cart</span></article>
  <article class="product"><div class="product-photo"><div class="shot" role="img" aria-label="Teal and tan two-tone tote" style="background:linear-gradient(90deg,#a65b2a,#1f6f88 30%,#1f6f88 70%,#a65b2a)"></div></div><h4>Products Name</h4><p>Lorem Ipsum is simply dummy text of the printing and typesetting industry.</p><div class="price">$149.99</div><span class="btn">Add to Cart</span></article>
</section>

<div class="about-band abs"></div>
<div class="about-photo abs" role="img" aria-label="Woman holding a coral quilted handbag"></div>
<section class="about-copy abs">
  <h2 class="display">About Us</h2>
  <p class="sub">SHORT LINES OF OUR COMPANY</p>
  <p class="body">Lorem Ipsum is simply dummy text of the printing and typesetting industry. Lorem Ipsum has been the industry's standard dummy text ever since the 1500s, when an unknown printer took a galley of type and scrambled it to make a type specimen book. It has survived not only five centuries, but also the leap into electronic typesetting, remaining essentially unchanged.</p>
  <span class="btn">Read More</span>
</section>

<div class="section-title abs" style="top:2013px"><h2 class="display">Latest Products</h2><p>EXPLORE THE BEST COLLECTION HERE</p></div>

<section class="product-grid abs" style="top:2097px">
  <article class="product"><div class="product-photo"><div class="shot" role="img" aria-label="Black textured dome handbag" style="background:linear-gradient(#3a3a3a,#0f0f0f)"></div></div><h4>Products Name</h4><p>Lorem Ipsum is simply dummy text of the printing and typesetting industry.</p><div class="price">$149.99</div><span class="btn">Add to Cart</span></article>
  <article class="product"><div class="product-photo"><div class="shot" role="img" aria-label="Red quilted structured handbag" style="width:140px;background:linear-gradient(#e0343a,#a5141a)"></div></div><h4>Products Name</h4><p>Lorem Ipsum is simply dummy text of the printing and typesetting industry.</p><div class="price">$149.99</div><span class="btn">Add to Cart</span></article>
  <article class="product"><div class="product-photo"><div class="shot" role="img" aria-label="Cream leather envelope clutch" style="height:95px;background:linear-gradient(#ece4d2,#cfc4ac)"></div></div><h4>Products Name</h4><p>Lorem Ipsum is simply dummy text of the printing and typesetting industry.</p><div class="price">$149.99</div><span class="btn">Add to Cart</span></article>
  <article class="product"><div class="product-photo"><div class="shot" role="img" aria-label="Mustard yellow top-handle tote" style="width:150px;background:linear-gradient(#f3c635,#d8a414)"></div></div><h4>Products Name</h4><p>Lorem Ipsum is simply dummy text of the printing and typesetting industry.</p><div class="price">$149.99</div><span class="btn">Add to Cart</span></article>
</section>

<section class="reviews abs" role="img" aria-label="Burgundy tote bag beside a seated person in jeans">
  <div class="reviews-inner">
    <h2 class="display">Reviews</h2>
    <p class="sub">OUR CUSTOMER SAY'S</p>
    <p class="quote">“ Lorem Ipsum is simply dummy text of the printing and typesetting industry. Lorem Ipsum has been the industry's standard dummy text ever since the 1500s, when an unknown printer took a galley of type and scrambled it to make a type specimen book. It has survived not only five centuries, but also the leap into electronic typesetting, remaining essentially unchanged. ”</p>
    <p class="author">MARA LINDELL</p>
    <p class="stars">★★★★★</p>
    <div class="dots"><span class="on"></span><span></span><span></span><span></span></div>
  </div>
  <svg class="slider-arrow abs" style="left:-2px;top:149px" viewBox="0 0 36 72"><path d="M0 0L36 36L0 72z" fill="#fff"/><path d="M10 31l-5 5 5 5" stroke="#999" stroke-width="1.5" fill="none"/></svg>
  <svg class="slider-arrow abs" style="right:0;top:149px" viewBox="0 0 36 72"><path d="M36 0L0 36L36 72z" fill="#fff"/><path d="M26 31l5 5-5 5" stroke="#0e5a47" stroke-width="2" fill="none"/></svg>
</section>

<div class="section-title abs" style="top:3110px"><h2 class="display">From the Blogs</h2><p style="letter-spacing:2px">OUR LATEST NEWS AND UPDATES</p></div>

<section class="blog-grid abs">
  <article class="post"><div class="post-photo" role="img" aria-label="Hand picking a tan handbag from a shelf" style="background:linear-gradient(100deg,#e9e4dc,#c7a27a 45%,#f2efe9 70%,#b8312c)"></div><p class="date">10.MAY.2020</p><h3>BLOG TITILE</h3><p>Lorem Ipsum is simply dummy text of the printing and typesetting industry. Lorem Ipsum has been the industry's standard dummy text ever since the 1500s.</p><p class="more">Read More</p></article>
  <article class="post"><div class="post-photo" role="img" aria-label="Woman walking on a city street carrying a quilted bag" style="background:linear-gradient(#c9c3b8,#8b8580 60%,#5f5c5a)"></div><p class="date">10.MAY.2020</p><h3>BLOG TITILE</h3><p>Lorem Ipsum is simply dummy text of the printing and typesetting industry. Lorem Ipsum has been the industry's standard dummy text ever since the 1500s.</p><p class="more">Read More</p></article>
  <article class="post"><div class="post-photo" role="img" aria-label="Woman in mustard shorts holding a brown handbag" style="background:linear-gradient(100deg,#8a5a3a,#c9924f 45%,#e9dcc8)"></div><p class="date">10.MAY.2020</p><h3>BLOG TITILE</h3><p>Lorem Ipsum is simply dummy text of the printing and typesetting industry. Lorem Ipsum has been the industry's standard dummy text ever since the 1500s.</p><p class="more">Read More</p></article>
</section>
<span class="btn browse abs">Browse More</span>

<div class="section-title abs" style="top:3855px"><h2 class="display">Signup for our Newsletter</h2><p style="letter-spacing:2px">CONNECT AND GET OUR UPDATES AND NEWS</p></div>
<form class="newsletter-form abs"><div class="field">Email Address</div><span class="btn">Subscribe</span></form>

<footer class="site-footer abs">
  <div class="footer-brand abs">
    <span class="brand-mark"></span>
    <div><div class="brand-name">MAISONLEAF</div><div class="brand-slogan">Your Slogan here</div></div>
  </div>
  <nav class="footer-nav abs"><span>Home</span><span>Handbags</span><span>Blog</span><span>About</span><span>Contact</span></nav>
  <div class="socials abs"><span></span><span></span><span></span><span></span><span></span><span></span></div>
  <div class="footer-rule abs"></div>
  <div class="payments abs"><span></span><span></span><span></span><span></span><span></span><span></span></div>
  <p class="legal abs">Privacy policy &nbsp;|&nbsp; Terms of use &nbsp;|&nbsp; Site map &nbsp;|&nbsp; Copyright © 2019 Maisonleaf. All Rights Reserved.</p>
</footer>

</body>
</html>
```